Brightfield Optics seeks updated contemporary business card

Brightfield Optics utilizes advanced technology and we take pride in the modern look and feel of our practice. We like our current card, but it's been four years so it is time for an update.

Target Market(s)

Females 25-45 make the most health care decisions for their family.

Contact Information for Business Card

Clean front. Back with info and with empty space for appointment time or other small note

Requirements
Must have
• Logo
Ridge Marketvale, 28413 E Larkspur Ave
Cedar Terrace Marketvale, 4638 S Dunmore Rd
Call or text: 509-342-1968
email: hello@brightfieldoptics.example
brightfieldoptics.example
Dr Tobias Werring & Associates

```html
<!DOCTYPE html>
<html lang="en">
<head>
<meta charset="utf-8">
<title>Brightfield Optics – Business Card</title>
<link rel="stylesheet" href="https://fonts.googleapis.com/css2?family=Open+Sans:wght@400;600;700;800&display=swap">
<style>
  :root {
    --page-bg: #e4e4e4;
    --card-bg: #f4f4f4;
    --card-edge: #d8d8d8;
    --navy: #1f3f6e;
    --accent-blue: #1b7fb3;
    --brand-blue: #0d8bc4;
    --brand-blue-deep: #1d5d92;
    --wash-blue: #d9e9f0;
    --text-dark: #2b2b2b;
  }
  html, body {
    margin: 0;
    width: 1200px;
    height: 960px;
    overflow: hidden;
    background: var(--page-bg);
    font-family: "Open Sans", Arial, sans-serif;
  }
  .canvas { position: relative; width: 1200px; height: 960px; }
  .card {
    position: absolute;
    left: 312px;
    width: 580px;
    height: 332px;
    background: var(--card-bg);
    border: 1px solid var(--card-edge);
    box-sizing: border-box;
    overflow: hidden;
    box-shadow: 2px 3px 5px rgba(0, 0, 0, 0.25);
  }
  .card--front { top: 125px; }
  .card--back { top: 507px; }

  .card-wash {
    position: absolute;
    inset: 0;
    background: radial-gradient(ellipse 330px 300px at 300px 330px,
      var(--wash-blue) 0%, var(--wash-blue) 55%, rgba(217, 233, 240, 0) 100%);
  }
  .card-sweep {
    position: absolute;
    left: 286px;
    top: 118px;
    width: 294px;
    height: 214px;
    background: radial-gradient(ellipse 300px 220px at 100% 100%,
      var(--brand-blue) 0%, var(--brand-blue-deep) 60%, rgba(29, 93, 146, 0) 100%);
  }

  .brand-name {
    margin: 0;
    font-weight: 800;
    font-size: 23px;
    letter-spacing: -0.3px;
    color: var(--navy);
    text-transform: uppercase;
    line-height: 1;
  }
  .brand-tagline {
    margin: 5px 0 0;
    font-weight: 700;
    font-size: 12px;
    color: var(--navy);
    text-transform: uppercase;
    line-height: 1;
  }
  .front-brand {
    position: absolute;
    right: 34px;
    top: 260px;
    text-align: center;
  }
  .back-brand {
    position: absolute;
    left: 39px;
    top: 101px;
    text-align: center;
  }

  .person {
    position: absolute;
    right: 29px;
    top: 54px;
    text-align: right;
  }
  .person-name {
    margin: 0;
    font-weight: 600;
    font-size: 18.5px;
    color: var(--accent-blue);
    line-height: 1.1;
  }
  .person-role {
    margin: 3px 0 0;
    font-size: 14px;
    color: var(--text-dark);
  }

  .practice {
    position: absolute;
    left: 38px;
    top: 174px;
    font-size: 14px;
    line-height: 20px;
    color: var(--text-dark);
  }
  .practice-name { margin: 0; color: var(--accent-blue); }
  .practice-location { margin: 0; }

  .contact-list {
    list-style: none;
    margin: 6px 0 0;
    padding: 0;
  }
  .contact-item {
    display: flex;
    align-items: center;
    gap: 4px;
    height: 20px;
  }
  .contact-icon { width: 13px; height: 13px; fill: var(--accent-blue); flex: none; }
</style>
</head>
<body>
<main class="canvas">

  <section class="card card--front" aria-label="Card front">
    <div class="card-wash" role="img" aria-label="Large faint brand decoration in pale blue"></div>
    <div class="front-brand">
      <p class="brand-name">Brightfield Optics</p>
      <p class="brand-tagline">Advanced Eye Care</p>
    </div>
  </section>

  <section class="card card--back" aria-label="Card back">
    <div class="card-sweep" role="img" aria-label="Blue brand decoration in the lower right corner"></div>

    <div class="back-brand">
      <p class="brand-name">Brightfield Optics</p>
      <p class="brand-tagline">Advanced Eye Care</p>
    </div>

    <div class="person">
      <p class="person-name">Daniel Harper</p>
      <p class="person-role">Founder</p>
    </div>

    <div class="practice">
      <p class="practice-name">Dr Tobias Werring &amp; Associates</p>
      <p class="practice-location">Ridge Marketvale, 28413 E Larkspur Ave</p>
      <p class="practice-location">Cedar Terrace Marketvale, 4638 S Dunmore Rd</p>
      <ul class="contact-list">
        <li class="contact-item">
          <svg class="contact-icon" viewBox="0 0 16 16" aria-hidden="true"><path d="M3.6 1.2l2.3 2.6-1.3 1.9c.9 2 2.6 3.7 4.6 4.6l1.9-1.3 2.6 2.3-1.4 2.4C6.8 14.9 1.1 9.2.9 3.8z"/></svg>
          <span>509-342-1968</span>
        </li>
        <li class="contact-item">
          <svg class="contact-icon" viewBox="0 0 16 16" aria-hidden="true"><path d="M1 3h14v10H1zm1.5 1.5v.3L8 9l5.5-4.2v-.3zm0 2.2v4.8h11V6.7L8 10.9z"/></svg>
          <span>hello@brightfieldoptics.example</span>
        </li>
        <li class="contact-item">
          <svg class="contact-icon" viewBox="0 0 16 16" aria-hidden="true"><path d="M8 1a7 7 0 100 14A7 7 0 008 1zm5.4 6.3h-2.5a11 11 0 00-1.1-4.6 5.6 5.6 0 013.6 4.6zM8 2.5c.7.9 1.4 2.6 1.5 4.8h-3C6.6 5.1 7.3 3.4 8 2.5zM6.2 2.7a11 11 0 00-1.1 4.6H2.6a5.6 5.6 0 013.6-4.6zM2.6 8.7h2.5a11 11 0 001.1 4.6 5.6 5.6 0 01-3.6-4.6zM8 13.5c-.7-.9-1.4-2.6-1.5-4.8h3c-.1 2.2-.8 3.9-1.5 4.8zm1.8-.2a11 11 0 001.1-4.6h2.5a5.6 5.6 0 01-3.6 4.6z"/></svg>
          <span>brightfieldoptics.example</span>
        </li>
      </ul>
    </div>
  </section>

</main>
</body>
</html>
```